Banner & also another minor digital image for an Online Academic Journal

A direct example of what I need can be found in this webpage: http://papers.tbhu-archive.org/qrvt/
(Please see attached files, "sAMPLE", and "sAMPLE 2", so you can see what I mean.)
This link (http://papers.tbhu-archive.org/qrvt/) is for an existing ONLINE ACADEMIC JOURNAL at the Thornbury Hill University.
It will help for you to be acquainted with the format of Online Academic Journals.
You will find that there is a banner on top as well as a digital image of a journal/book cover on the right.
I need a
(1) banner and
a (2) digital journal/book cover
for a website for an ONLINE ACADEMIC JOURNAL.
I am looking for a serious, professional, elegant design.
There will not be a print version. Only web-based online publication. No coding needed, only PSD, JPG/PNG and PDF.
1) We use PelloWave (http://archives.pellowave.com/repository-software/journals/) for the digital image of the journal/book cover layout. Link shows the general layout of the journal website.
2) For the digital image of the journal/book cover and also the banner,
Name of the journal is....
"Lumen: A Quarterly of Civic Ethics and Recovery Work"
Only this text will be used and applied to both banner and cover.
***The color associated with the theme of dignity is purple
****You could also add the color red.
*****I don't want the design to be garish, but accents in red might represent
the sexual exploitation and violence in the title.
3) Attached "sAmple 2" file is a basic design for the digital image of the journal/book cover from PelloWave. I am looking for something more elegant and professional looking. Your creativity is encouraged. I am open to receiving your interpretation.
Target Market(s)
Academics & Community Professionals
Industry/Entity Type
Non Profit
Contact Information for Business Card
Match journal design

```html
<!DOCTYPE html>
<html lang="en">
<head>
<meta charset="utf-8">
<title>Lumen — A Quarterly of Civic Ethics and Recovery Work</title>
<link rel="stylesheet" href="https://fonts.googleapis.com/css2?family=EB+Garamond:wght@400;500;600&display=swap">
<style>
  :root {
    --purple: #876aab;
    --red: #f04e52;
    --paper: #ffffff;
    --shadow: rgba(60, 20, 40, 0.45);
  }
  * { margin: 0; padding: 0; box-sizing: border-box; }
  html, body {
    width: 819px;
    height: 1200px;
    overflow: hidden;
    background: var(--paper);
  }
  .cover {
    position: relative;
    width: 819px;
    height: 1200px;
    background: var(--paper);
    font-family: "EB Garamond", Garamond, "Times New Roman", serif;
  }
  .band { position: absolute; left: 0; width: 100%; }
  .band--masthead {
    top: 0;
    height: 463px;
    background: var(--purple);
    display: flex;
    align-items: center;
    justify-content: center;
  }
  .band--subtitle {
    top: 476px;
    height: 620px;
    background: var(--red);
    display: flex;
    align-items: center;
    justify-content: center;
  }
  .band--foot {
    top: 1110px;
    height: 90px;
    background: var(--purple);
  }
  .journal-title {
    margin-top: 40px;
    font-size: 188px;
    font-weight: 500;
    line-height: 1;
    letter-spacing: 2px;
    color: var(--red);
    text-shadow: 2px 3px 4px var(--shadow);
  }
  .journal-subtitle {
    list-style: none;
    text-align: center;
    font-size: 46px;
    font-weight: 600;
    line-height: 68px;
    letter-spacing: 0.5px;
    color: var(--paper);
    text-shadow: 2px 3px 3px var(--shadow);
  }
</style>
</head>
<body>
  <main class="cover">
    <header class="band band--masthead">
      <h1 class="journal-title">LUMEN</h1>
    </header>
    <section class="band band--subtitle">
      <ul class="journal-subtitle">
        <li>A</li>
        <li>QUARTERLY</li>
        <li>OF</li>
        <li>CIVIC ETHICS</li>
        <li>AND</li>
        <li>RECOVERY</li>
        <li>WORK</li>
      </ul>
    </section>
    <footer class="band band--foot"></footer>
  </main>
</body>
</html>
```